Pub/Bar snack and nibbles packaging

What we want:
We require professional packaging design for our jerky range.

About us and why we're here:
We're a husband and wife team from a small town who has been supplying artesian dried meats to local pubs/bars in outback Australia. Through word of mouth our volume has been growing steadily these few years. We seek someone who can assist provide a packaging range that best represents what great products my wife and I have been producing. And ultimately, a packaging that this product deserves. We have attached pictures of bar/pubs to give an idea of where our product is typically placed.

Target Market(s)

Target market:
Our customers are patrons of country motels / pubs and convenience stores. Our jerky goes particularly well with a cold beer.

Industry/Entity Type

It Professional

Requirements
Must have
• Specifics:
• Business Name: Quandong Meats. Artisan Style.
• Product: Beef Chunks (we have 4 different flavours original, spicy, honey, pepper. The design should be easily changeable to accomodate different flavours)
• Description: Made from 100% Australian Beef
• Typography: We have attached some fonts for inspiration (e.g., copper heron, other alcohol brands)
• Packet Size: 110mm (w) x 170mm (l)
• We also require the back of the packaging designed as well. That information will be provided to the winning designer chosen.
Nice to have
• Design Concept:
• The design should tell a story which features an outback or bush setting. We have provided a few examples for inspiration (e.g., jackaroo walking with working dog, on a horse, swagman camping) or come up with your own. We will decide the final design based on the story that we can most related to.
Should not have
• We do not want any photo images on this design, illustrations and text only.

```html
<!DOCTYPE html>
<html lang="en">
<head>
<meta charset="utf-8">
<title>Quandong Meats – Jerky Range</title>
<link href="https://fonts.googleapis.com/css2?family=Staatliches&family=Smokum&display=swap" rel="stylesheet">
<style>
  :root {
    --brand-red: #9a4545;
    --jerky-red: #8e1f24;
    --charcoal: #555759;
    --charcoal-dark: #4a4c4e;
    --ink: #3e3f41;
    --paper: #f3f1ec;
    --kraft: #c49a6c;
    --kraft-dark: #b58a5c;
    --honey: #8a3322;
    --original: #e0626a;
    --spicy: #4f8b38;
    --white: #ffffff;
    --pale: #dcdcdc;
  }
  * { box-sizing: border-box; margin: 0; padding: 0; }
  html, body { width: 1200px; height: 1200px; overflow: hidden; background: var(--white); }
  .canvas { position: relative; width: 1200px; height: 1200px; }

  .brand-lockup {
    position: absolute; left: 30px; top: 60px; width: 410px; text-align: center;
  }
  .brand-lockup .brand-rule { height: 3px; background: var(--charcoal); margin-bottom: 14px; }
  .brand-name {
    font-family: "Staatliches", sans-serif; color: var(--charcoal);
    font-size: 56px; letter-spacing: 2px; line-height: 1;
  }

  .pouch {
    position: absolute; width: 330px; height: 560px;
    background: linear-gradient(180deg, var(--kraft) 0%, var(--kraft-dark) 100%);
    border-radius: 6px;
  }
  .pouch::before {
    content: ""; position: absolute; left: 0; right: 0; top: 0; height: 44px;
    border-bottom: 2px solid rgba(0,0,0,0.08);
  }
  .pouch.honey { left: 225px; top: 322px; }
  .pouch.spicy { left: 745px; top: 322px; }
  .pouch.original { left: 466px; top: 358px; z-index: 2; box-shadow: 0 6px 18px rgba(0,0,0,0.18); }

  .label {
    position: absolute; left: 24px; right: 24px; top: 102px; height: 370px;
    background: var(--paper); padding: 14px 16px;
  }
  .label-frame {
    border: 1.5px solid var(--ink); height: 100%;
    display: flex; flex-direction: column; align-items: center;
  }
  .label-brand {
    margin-top: 60px; width: 100%; text-align: center;
    border-top: 1.5px solid var(--ink); padding-top: 6px;
    font-family: "Staatliches", sans-serif; color: var(--charcoal);
    font-size: 30px; letter-spacing: 1px; line-height: 1;
  }
  .product-title { display: flex; align-items: center; gap: 6px; margin-top: 8px; }
  .product-title svg { width: 36px; height: 12px; }
  .jerky {
    font-family: "Smokum", serif; color: var(--jerky-red);
    font-size: 62px; line-height: 0.95;
    border-top: 2px solid var(--jerky-red); padding-top: 2px;
  }
  .artisan {
    font-family: "Smokum", serif; color: var(--jerky-red);
    font-size: 22px; letter-spacing: 1px;
    border-bottom: 2px solid var(--jerky-red); line-height: 1.1;
  }
  .origin-badge {
    margin-top: 8px; background: var(--charcoal); color: var(--white);
    font-family: "Staatliches", sans-serif; font-size: 16px; line-height: 1.05;
    text-align: center; padding: 4px 16px; border-radius: 4px;
    outline: 1.5px solid var(--charcoal); outline-offset: 2px;
  }
  .flavour-row {
    width: 100%; margin-top: 12px; border-top: 1.5px solid var(--ink);
    border-bottom: 1.5px solid var(--ink); padding: 10px 0; display: flex; justify-content: center;
  }
  .flavour {
    font-family: "Staatliches", sans-serif; color: var(--white); font-size: 17px;
    letter-spacing: 1px; width: 170px; text-align: center; padding: 2px 0;
    clip-path: polygon(0 0, 100% 0, 95% 50%, 100% 100%, 0 100%, 5% 50%);
  }
  .honey .flavour { background: var(--honey); }
  .original .flavour { background: var(--original); }
  .spicy .flavour { background: var(--spicy); }
  .net-weight {
    font-family: "Staatliches", sans-serif; color: var(--ink);
    font-size: 18px; letter-spacing: 1px; margin-top: 12px;
  }

  .brand-panel {
    position: absolute; left: 734px; top: 922px; width: 438px; height: 250px;
    background: var(--charcoal-dark);
  }
  .brand-panel .brand-rule { position: absolute; left: 0; right: 0; top: 140px; height: 2px; background: var(--pale); }
  .brand-panel .brand-name {
    position: absolute; left: 0; right: 0; top: 160px; text-align: center;
    color: var(--white); font-size: 58px;
  }
</style>
</head>
<body>
<main class="canvas">

  <section class="brand-lockup">
    <div class="brand-rule"></div>
    <div class="brand-name">Quandong Meats</div>
  </section>

  <article class="pouch honey">
    <div class="label"><div class="label-frame">
      <div class="label-brand">Quandong Meats</div>
      <div class="product-title">
        <svg viewBox="0 0 36 12"><path d="M0 6h30M24 1l6 5-6 5M0 2l4 4-4 4" fill="none" stroke="#777" stroke-width="1.5"/></svg>
        <div class="jerky">JERKY</div>
        <svg viewBox="0 0 36 12"><path d="M36 6H6M12 1L6 6l6 5M36 2l-4 4 4 4" fill="none" stroke="#777" stroke-width="1.5"/></svg>
      </div>
      <div class="artisan">ARTISAN STYLE</div>
      <div class="origin-badge">Made from 100%<br>Australian Beef</div>
      <div class="flavour-row"><div class="flavour">Honey</div></div>
      <div class="net-weight">100 GR.</div>
    </div></div>
  </article>

  <article class="pouch spicy">
    <div class="label"><div class="label-frame">
      <div class="label-brand">Quandong Meats</div>
      <div class="product-title">
        <svg viewBox="0 0 36 12"><path d="M0 6h30M24 1l6 5-6 5M0 2l4 4-4 4" fill="none" stroke="#777" stroke-width="1.5"/></svg>
        <div class="jerky">JERKY</div>
        <svg viewBox="0 0 36 12"><path d="M36 6H6M12 1L6 6l6 5M36 2l-4 4 4 4" fill="none" stroke="#777" stroke-width="1.5"/></svg>
      </div>
      <div class="artisan">ARTISAN STYLE</div>
      <div class="origin-badge">Made from 100%<br>Australian Beef</div>
      <div class="flavour-row"><div class="flavour">Spicy</div></div>
      <div class="net-weight">100 GR.</div>
    </div></div>
  </article>

  <article class="pouch original">
    <div class="label"><div class="label-frame">
      <div class="label-brand">Quandong Meats</div>
      <div class="product-title">
        <svg viewBox="0 0 36 12"><path d="M0 6h30M24 1l6 5-6 5M0 2l4 4-4 4" fill="none" stroke="#777" stroke-width="1.5"/></svg>
        <div class="jerky">JERKY</div>
        <svg viewBox="0 0 36 12"><path d="M36 6H6M12 1L6 6l6 5M36 2l-4 4 4 4" fill="none" stroke="#777" stroke-width="1.5"/></svg>
      </div>
      <div class="artisan">ARTISAN STYLE</div>
      <div class="origin-badge">Made from 100%<br>Australian Beef</div>
      <div class="flavour-row"><div class="flavour">Original</div></div>
      <div class="net-weight">100 GR.</div>
    </div></div>
  </article>

  <section class="brand-panel">
    <div class="brand-rule"></div>
    <div class="brand-name">Quandong Meats</div>
  </section>

</main>
</body>
</html>
```